EPS Recycling Rpt

Our annual recycling rate report needs a tune up. Our organization helps faciltate expanded polystyrene (EPS) recycling and this 4-page report highlights growth trends and useful information to help readers understand the dynamics of EPS recycling. We need a designer that can recreate the brochure we've published over the past several years with some minor adjustments to accomodate new content.

A PDF of the 2012 report is attached. Header text should reflect 2013 in all cases. Please pay close attention to the new placement of the copy as indicated in the Word file (also attached) as it has been significantly modified from the 2012 version. The color pallette for our branding is provided. Contact us with any questions.

```html
<!DOCTYPE html>
<html lang="en">
<head>
<meta charset="utf-8">
<title>2013 EPS Recycling Rate Report</title>
<link href="https://fonts.googleapis.com/css2?family=Oswald:wght@500;600&family=PT+Sans+Narrow:wght@400;700&family=Source+Sans+3:wght@400;600;700&display=swap" rel="stylesheet">
<style>
  :root {
    --orange: #f2861e;
    --orange-light: #f6a15a;
    --blue: #4a84a8;
    --blue-dark: #3d7099;
    --panel: #5689a9;
    --gold: #a88a2a;
    --soil: #3a3430;
    --soil-dark: #1f1b19;
    --green: #6fbf44;
    --text: #3b3b3b;
    --axis: #6a6a6a;
  }
  * { box-sizing: border-box; margin: 0; padding: 0; }
  html, body { width: 927px; height: 1200px; overflow: hidden; }
  body {
    position: relative;
    background: linear-gradient(#ffffff 0%, #ffffff 60%, #ececec 100%);
    font-family: "PT Sans Narrow", "Arial Narrow", sans-serif;
    color: var(--text);
  }
  .brand {
    position: absolute; left: 57px; top: 28px;
    display: flex; align-items: center; gap: 14px;
  }
  .brand-dot {
    width: 92px; height: 92px; border-radius: 50%;
    background: var(--gold);
  }
  .brand-name {
    font-family: "Source Sans 3", sans-serif;
    font-weight: 600; font-size: 25px; line-height: 1.05;
    color: var(--gold); width: 170px;
  }
  .hero-photo {
    position: absolute; left: 0; top: 183px; width: 927px; height: 316px;
    background: radial-gradient(ellipse at 22% 55%, #4f6b2c 0%, #3f4a26 14%, var(--soil) 30%, var(--soil-dark) 100%);
  }
  .title-tab {
    position: absolute; left: 590px; top: 0; width: 317px; height: 297px;
    background: var(--orange);
    box-shadow: -3px 4px 8px rgba(0,0,0,.25);
    text-align: center;
    font-family: "Oswald", "Arial Narrow", sans-serif;
    font-weight: 600; color: #fff; line-height: 1;
    padding-top: 28px;
    overflow: hidden;
  }
  .title-tab .line { display: block; white-space: nowrap; }
  .title-tab .line span { display: inline-block; transform: scaleY(1.22); transform-origin: center top; }
  .title-tab .t1 { font-size: 66px; height: 90px; letter-spacing: 1px; }
  .title-tab .t2 { font-size: 62px; height: 82px; }
  .title-tab .t3 { font-size: 52px; height: 70px; }
  .intro {
    position: absolute; left: 48px; top: 520px; width: 859px;
  }
  .intro h2 {
    font-family: "Oswald", sans-serif; font-weight: 500;
    font-size: 23px; color: var(--blue-dark); margin-bottom: 6px;
  }
  .intro p { font-size: 12px; line-height: 1.48; margin-bottom: 14px; }
  .figure-title {
    position: absolute; left: 48px; top: 880px;
    font-family: "Oswald", sans-serif; font-weight: 500;
    font-size: 22px; line-height: 1.55; color: var(--blue-dark);
  }
  .figure-title span { display: block; padding-left: 75px; }
  .chart { position: absolute; left: 20px; top: 945px; }
  .chart .ylabel { font-family: "Oswald", sans-serif; font-weight: 500; fill: var(--blue-dark); font-size: 12px; }
  .chart .ytick { font-family: "Oswald", sans-serif; font-weight: 500; font-size: 13px; fill: var(--axis); }
  .chart .xtick { font-family: "Source Sans 3", sans-serif; font-weight: 700; font-size: 9px; fill: var(--axis); }
  .table-panel { position: absolute; left: 591px; top: 885px; width: 316px; height: 292px; }
  .table-panel svg { position: absolute; inset: 0; }
  .table-body {
    position: absolute; left: 24px; top: 80px; width: 270px; color: #fff;
    font-family: "Source Sans 3", sans-serif;
  }
  .table-body h3 { font-weight: 700; font-size: 21px; line-height: 1.3; }
  .table-body .unit { font-size: 20px; margin-bottom: 22px; }
  .row { display: flex; align-items: baseline; font-size: 21px; line-height: 1.55; }
  .row .leader { flex: 1; border-bottom: 1px solid #fff; margin: 0 6px; }
</style>
</head>
<body>
  <div class="brand">
    <div class="brand-dot"></div>
    <div class="brand-name">Polyfoam Recovery Council</div>
  </div>

  <div class="hero-photo" role="img" aria-label="Photo of two hands cupping a heart shape made of green sprouts on dark soil"></div>

  <div class="title-tab">
    <div class="line t1"><span>2013 EPS</span></div>
    <div class="line t2"><span>RECYCLING</span></div>
    <div class="line t3"><span>RATE REPORT</span></div>
  </div>

  <section class="intro">
    <h2>MANY ARE NOT AWARE EXPANDED POLYSTYRENE (EPS) PACKAGING IS RECYCLABLE</h2>
    <p>And is being recycled successfully by businesses and consumers throughout the United States. The 2012 Expanded Polystyrene Recycling Rate Study (the “Rate Study”) was conducted by the Polyfoam Recovery Council (PRC). To better track EPS recycling trends PRC gathers data to reflect both post-commercial and post-residential collection streams. Based on data received from forty-one EPS manufacturers and independent recyclers in the U.S., the 2013 results reflect a modest decrease in the amount of post-industrial pounds recycled and a substantial increase in the number of post-consumer pounds recycled.</p>
    <p>As reflected in Table 1, more than 125 million pounds of EPS was recycled during calendar year 2013. This figure includes 72.8 million pounds of post-commercial and post-consumer packaging and 54.5 million pounds of post-industrial recovery. Post-consumer and post-commercial recycling are defined as any material that is recycled after its intended end-use – while post-industrial recovery includes EPS facility scrap that is recycled but never served its intended purpose as a packaging material or other end-use application.</p>
    <p>Since 1991, EPS recycling has demonstrated stable, incremental growth and steady end-use market developments. This growth can be attributed to innovative and sustainable programs specifically geared to EPS recycling. Businesses and consumers play a key role in reducing the amount of packaging material that enters the waste stream by contributing to a shared-responsibility approach to recycling.</p>
    <p>As compared to the 2012 Rate Study, 2013 showed a notable growth for post-consumer and post-commercial recycling. This is supported by a strong reliance on high volume sources and proves the success of industry recycling efforts in the United States. Advances in EPS recycling technologies, collaborative collection programs and new end-use markets have continued to broaden EPS recycling opportunities. In addition, the EPS industry fosters ongoing development of new and innovative recycling initiatives that will promote further EPS recycling growth. These include recycled content resin and unique volume reduction technologies that are showing great potential.</p>
  </section>

  <div class="figure-title">FIGURE 1: DOMESTIC POST-CONSUMER EPS RECYCLING<span>(1990-2013)</span></div>

  <svg class="chart" width="530" height="170" viewBox="0 0 530 170">
    <defs>
      <linearGradient id="barFill" x1="0" y1="0" x2="0" y2="1">
        <stop offset="0" stop-color="#f6a15a"/>
        <stop offset="1" stop-color="#ee8a3a"/>
      </linearGradient>
    </defs>
    <text class="ylabel" transform="translate(19 150) rotate(-90)" textLength="145" lengthAdjust="spacingAndGlyphs">MILLIONS OF POUNDS RECYCLED</text>
    <g text-anchor="end">
      <text class="ytick" x="48" y="140">0</text>
      <text class="ytick" x="48" y="124.5">10</text>
      <text class="ytick" x="48" y="109">20</text>
      <text class="ytick" x="48" y="93.5">30</text>
      <text class="ytick" x="48" y="78">40</text>
      <text class="ytick" x="48" y="62.5">50</text>
      <text class="ytick" x="48" y="47">60</text>
      <text class="ytick" x="48" y="31.5">70</text>
      <text class="ytick" x="48" y="16">80</text>
    </g>
    <g fill="url(#barFill)">
      <rect x="68" y="132" width="22" height="3"/>
      <rect x="103.5" y="104" width="22" height="31"/>
      <rect x="139" y="97.8" width="22" height="37.2"/>
      <rect x="174.5" y="100.9" width="22" height="34.1"/>
      <rect x="210" y="105.5" width="22" height="29.5"/>
      <rect x="245.5" y="96.2" width="22" height="38.8"/>
      <rect x="281" y="94.7" width="22" height="40.3"/>
      <rect x="316.5" y="96.2" width="22" height="38.8"/>
      <rect x="352" y="85.4" width="22" height="49.6"/>
      <rect x="387.5" y="82.3" width="22" height="52.7"/>
      <rect x="423" y="77.7" width="22" height="57.3"/>
      <rect x="458.5" y="77.7" width="22" height="57.3"/>
      <rect x="494" y="22.2" width="22" height="112.8"/>
    </g>
    <path d="M56 10 V135 H524" fill="none" stroke="var(--axis)" stroke-width="2"/>
    <g text-anchor="middle">
      <text class="xtick" x="79" y="152">1990</text>
      <text class="xtick" x="114.5" y="152">1992</text>
      <text class="xtick" x="150" y="152">1994</text>
      <text class="xtick" x="185.5" y="152">1996</text>
      <text class="xtick" x="221" y="152">1998</text>
      <text class="xtick" x="256.5" y="152">2000</text>
      <text class="xtick" x="292" y="152">2002</text>
      <text class="xtick" x="327.5" y="152">2004</text>
      <text class="xtick" x="363" y="152">2006</text>
      <text class="xtick" x="398.5" y="152">2008</text>
      <text class="xtick" x="434" y="152">2010</text>
      <text class="xtick" x="469.5" y="152">2012</text>
      <text class="xtick" x="505" y="152">2013</text>
    </g>
  </svg>

  <div class="table-panel">
    <svg width="316" height="292" viewBox="0 0 316 292">
      <path d="M0 26 L316 0 V292 H0 Z" fill="var(--panel)"/>
      <circle cx="274" cy="50" r="44" fill="#ffffff"/>
      <circle cx="274" cy="50" r="40" fill="var(--green)"/>
    </svg>
    <div class="table-body">
      <h3>Table 1:<br>2013 Domestic EPS Recycling</h3>
      <div class="unit">(millions of pounds)</div>
      <div class="row"><span>Post-Consumer</span><span class="leader"></span><span>72.8</span></div>
      <div class="row"><span>Post-Industrial</span><span class="leader"></span><span>54.5</span></div>
      <div class="row"><span>Total EPS Recycling</span><span class="leader"></span><span>127.3</span></div>
    </div>
  </div>
</body>
</html>
```